Church Grand Opening Bill Board design

I would like to create a bill board design for our church's grand opening. I would like to incorporate pictures of two separate preachers with a creative way of blending them both together so it won't take up too much space. I have included pictures and logo.

I am open for color coordination and I have included a couple of past designs to use as a reference

The information I would want on the Build Board is the following (1) Grand Opening (2) 4218 E. Marlowe Avenue (3) 10:30am (4) Multi-Ethnic Church Planting Church (5) Sept. 26, 2021

Target Market(s)

Church shoppers and those who have never been connected to a church

Font styles to use
Serif

Requirements
Must have
• Our Logo
Nice to have
• i do not want any crosses or religious symbols

```html
<!DOCTYPE html>
<html lang="en">
<head>
<meta charset="UTF-8">
<title>Evergrow Church Grand Opening Billboard</title>
<link rel="stylesheet" href="https://fonts.googleapis.com/css2?family=Cinzel:wght@500;600&family=Marcellus&family=Source+Serif+4:wght@600;700&display=swap">
<style>
  :root {
    --backdrop: #d4d4d4;
    --board: #000000;
    --orange: #f7962b;
    --white: #ffffff;
    --ink: #111111;
  }
  * { box-sizing: border-box; margin: 0; padding: 0; }
  html, body {
    width: 977px; height: 1200px; overflow: hidden;
    background: var(--backdrop);
  }
  .billboard {
    position: absolute; left: 20px; top: 366px;
    width: 937px; height: 467px;
    background: var(--board); overflow: hidden;
  }
  .photo-art {
    position: absolute; inset: 0; width: 937px; height: 467px;
  }
  .brand {
    position: absolute; left: 150px; top: 64px; width: 260px;
    display: flex; align-items: center; justify-content: center; gap: 10px;
    font-family: "Cinzel", serif; font-weight: 600; font-size: 30px;
    color: var(--orange); letter-spacing: 1px;
  }
  .brand-dot {
    width: 16px; height: 16px; border-radius: 50%; background: var(--orange);
  }
  .headline {
    position: absolute; left: 40px; width: 480px; text-align: center;
    font-family: "Cinzel", serif; font-weight: 500; color: var(--white);
    line-height: 1;
  }
  .headline-grand { top: 160px; font-size: 88px; }
  .headline-opening { top: 238px; font-size: 96px; letter-spacing: -1px; }
  .address-band {
    position: absolute; left: 47px; top: 335px; width: 452px; height: 49px;
    background: var(--orange);
    display: flex; align-items: center; gap: 10px; padding-left: 14px;
    font-family: "Source Serif 4", serif; font-weight: 700; font-size: 31px;
    color: var(--ink);
  }
  .address-band svg { width: 18px; height: 26px; flex: none; }
  .facts {
    position: absolute; left: 75px; top: 394px;
    display: flex; align-items: center; gap: 10px;
  }
  .tags { list-style: none; font-family: "Marcellus", serif; font-size: 19px; color: var(--white); line-height: 25px; }
  .tags li { display: flex; align-items: center; gap: 6px; }
  .tags svg { width: 16px; height: 16px; }
  .divider { width: 1px; height: 42px; background: var(--white); margin: 0 4px; }
  .when { display: flex; align-items: center; gap: 6px; }
  .when svg { width: 42px; height: 42px; }
  .when-text {
    font-family: "Source Serif 4", serif; font-weight: 700; font-size: 19px;
    color: var(--white); line-height: 23px;
  }
</style>
</head>
<body>
<main class="billboard">
  <svg class="photo-art" viewBox="0 0 1364 680" preserveAspectRatio="none">
    <defs>
      <linearGradient id="stage" x1="0" y1="0" x2="1" y2="1">
        <stop offset="0" stop-color="#3a1a2a"/>
        <stop offset="0.5" stop-color="#1c1418"/>
        <stop offset="1" stop-color="#5a3a20"/>
      </linearGradient>
      <linearGradient id="studio" x1="0" y1="0" x2="0" y2="1">
        <stop offset="0" stop-color="#ffffff"/>
        <stop offset="1" stop-color="#e9e9ec"/>
      </linearGradient>
    </defs>
    <circle cx="1300" cy="500" r="380" fill="var(--orange)"/>
    <circle cx="1275" cy="250" r="250" fill="var(--orange)"/>
    <circle cx="1130" cy="560" r="290" fill="var(--orange)"/>
    <circle cx="1130" cy="560" r="265" fill="url(#stage)" role="img" aria-label="Photo of a preacher speaking on a stage with guitars behind"/>
    <circle cx="1275" cy="250" r="225" fill="url(#studio)" role="img" aria-label="Photo of a preacher with a headset microphone gesturing"/>
  </svg>

  <div class="brand"><span class="brand-dot"></span>Evergrow Church</div>

  <h1 class="headline headline-grand">GRAND</h1>
  <p class="headline headline-opening">OPENING</p>

  <div class="address-band">
    <svg viewBox="0 0 18 26"><path d="M9 0C4 0 0 4 0 9c0 7 9 17 9 17s9-10 9-17C18 4 14 0 9 0zm0 13a4 4 0 1 1 0-8 4 4 0 0 1 0 8z" fill="var(--white)"/></svg>
    4218 E. Marlowe Avenue
  </div>

  <div class="facts">
    <ul class="tags">
      <li><svg viewBox="0 0 16 16"><circle cx="8" cy="8" r="8" fill="var(--orange)"/><path d="M4 8.5l2.7 2.5L12 5.5" stroke="var(--white)" stroke-width="2" fill="none"/></svg>Planting Church</li>
      <li><svg viewBox="0 0 16 16"><circle cx="8" cy="8" r="8" fill="var(--orange)"/><path d="M4 8.5l2.7 2.5L12 5.5" stroke="var(--white)" stroke-width="2" fill="none"/></svg>Multi-Ethnic Church</li>
    </ul>
    <span class="divider"></span>
    <div class="when">
      <svg viewBox="0 0 42 42" fill="none" stroke="var(--orange)" stroke-width="2.5">
        <circle cx="21" cy="23" r="15"/>
        <path d="M21 14v9h7M8 9l6-4M34 9l-6-4M11 38l3-3M31 38l-3-3"/>
      </svg>
      <div class="when-text">10:30am<br>Sept. 26, 2021</div>
    </div>
  </div>
</main>
</body>
</html>
```